Business card for plumber

I need a business card for my plumbing company.
on it should:
Surname
position
E-mail
Telephone & mobile phone
Website
Please everything as placeholders / fantasy names.
We stand for high quality, hygiene and professionalism.

Colours:
# 606060 anthracite
# f7931e orange
# 2b89cc blue

Industry/Entity Type

Plumber

Contact Information for Business Card

folgt...

```html
<!DOCTYPE html>
<html lang="de">
<head>
<meta charset="utf-8">
<title>Brannwald Haustechnik – Visitenkarte</title>
<link rel="stylesheet" href="https://fonts.googleapis.com/css2?family=Montserrat:wght@700&family=Roboto:wght@400&display=swap">
<style>
  :root {
    --anthracite: #606060;
    --orange: #f7931e;
    --blue: #2b89cc;
    --paper: #ffffff;
    --backdrop: #d9d8d5;
    --rule: #4a4a4a;
  }
  * { box-sizing: border-box; margin: 0; padding: 0; }
  html, body { width: 1200px; height: 801px; overflow: hidden; }
  body {
    background: var(--backdrop);
    display: flex;
    align-items: center;
    justify-content: center;
    gap: 40px;
    font-family: "Roboto", Arial, sans-serif;
  }
  .card {
    width: 540px;
    height: 309px;
    box-shadow: 0 6px 18px rgba(0,0,0,.18);
    position: relative;
  }
  .card--front {
    background: var(--paper);
    display: flex;
    align-items: center;
  }
  .card--back {
    background: var(--blue);
    display: flex;
    align-items: center;
    justify-content: center;
  }
  .brand {
    display: flex;
    align-items: center;
    gap: 10px;
    font-family: "Montserrat", Arial, sans-serif;
    font-weight: 700;
    text-transform: uppercase;
    line-height: 1.05;
  }
  .brand__dot {
    width: 14px; height: 14px; border-radius: 50%;
    flex: none;
  }
  .card--front .brand { width: 270px; justify-content: center; color: var(--blue); font-size: 19px; }
  .card--front .brand__dot { background: var(--blue); }
  .card--back .brand { color: var(--paper); font-size: 36px; gap: 16px; }
  .card--back .brand__dot { background: var(--paper); width: 22px; height: 22px; }
  .divider {
    width: 1px;
    height: 140px;
    background: var(--rule);
    flex: none;
  }
  .contact { padding-left: 26px; }
  .contact__name {
    font-family: "Montserrat", Arial, sans-serif;
    font-weight: 700;
    font-size: 19px;
    color: var(--blue);
    text-transform: uppercase;
  }
  .contact__role {
    font-family: "Montserrat", Arial, sans-serif;
    font-weight: 700;
    font-size: 15px;
    color: var(--orange);
    margin-bottom: 14px;
  }
  .contact__list { list-style: none; }
  .contact__item {
    display: flex;
    align-items: center;
    gap: 8px;
    font-size: 14px;
    color: var(--anthracite);
    line-height: 21px;
  }
  .contact__icon { width: 13px; height: 13px; flex: none; fill: var(--blue); }
</style>
</head>
<body>
  <section class="card card--front">
    <div class="brand"><span class="brand__dot"></span><span>Brannwald<br>Haustechnik</span></div>
    <div class="divider"></div>
    <div class="contact">
      <p class="contact__name">Lukas Verhoeven</p>
      <p class="contact__role">Managing Director</p>
      <ul class="contact__list">
        <li class="contact__item">
          <svg class="contact__icon" viewBox="0 0 16 16"><rect x="4" y="1" width="8" height="14" rx="1.5"/><rect x="5.5" y="3" width="5" height="8" fill="#fff"/></svg>
          555.210.4837
        </li>
        <li class="contact__item">
          <svg class="contact__icon" viewBox="0 0 16 16"><path d="M3 2l3 0 1 3-2 1.5c1 2 2.5 3.5 4.5 4.5L11 9l3 1v3c0 .6-.4 1-1 1C7.5 14 2 8.5 2 3c0-.6.4-1 1-1z"/></svg>
          555.210.4800
        </li>
        <li class="contact__item">
          <svg class="contact__icon" viewBox="0 0 16 16"><rect x="1" y="3" width="14" height="10" rx="1"/><path d="M1.5 3.5L8 9l6.5-5.5" stroke="#fff" stroke-width="1.3" fill="none"/></svg>
          info@brannwaldhk.com
        </li>
        <li class="contact__item">
          <svg class="contact__icon" viewBox="0 0 16 16"><circle cx="8" cy="8" r="7"/><path d="M1 8h14M8 1c-3 3-3 11 0 14M8 1c3 3 3 11 0 14" stroke="#fff" stroke-width="1" fill="none"/></svg>
          www.brannwaldhk.com
        </li>
      </ul>
    </div>
  </section>
  <section class="card card--back">
    <div class="brand"><span class="brand__dot"></span><span>Brannwald<br>Haustechnik</span></div>
  </section>
</body>
</html>
```